Improving a camping website homepage header*

My client is very happy with his new website and its new functionalities. However, he's not very happy about the homepage design. Specifically, the header(this includes the menu, large header image and two columns beneath that). You can find the website here: http://lnkvo.example/siteTentra .

He forwarded me several other websites he likes. Which can be found in the attachments. I also included several pictures of the camping.

I'm looking for a design that will improve the header of the homepage with room for other global style chances. The logo cannot be changed.

Attachments
1) His old website homepage
2) Website mockup he liked.
3) Another website mockup he liked.

Other images can be found on the new website http://lnkvo.example/siteTentra or his old website http://lnkvo.example/formerSiteTentra.

Can you help us?
Updates

Hello guys. Here's a bit more information - Language used on the website is dutch. - The two columns left/right are supposed to link to Hire/Buy chalets. The client indicated that he finds these links important, but doesn't like the current design. I think this is partially the case because he doesn't like the icons. I'm looking forward to your designs!

Target Market(s)

30-50 year old wealthy people that want to purchase or rent cabins in the Netherlands.

Number of Pages Required

1 page

Colors

Designer to choose colors to be used in the design.

Requirements
Must have
• Improved header
Nice to have
• Global style changes
Should not have
• Logo changes

```html
<!DOCTYPE html>
<html lang="nl">
<head>
<meta charset="utf-8">
<title>Parc Lindehof – Chalet huren</title>
<link href="https://fonts.googleapis.com/css2?family=Open+Sans:wght@400;600&display=swap" rel="stylesheet">
<style>
  :root {
    --green: #6cb22f;
    --dark: #2d3540;
    --text: #3a3f45;
    --white: #ffffff;
    --border: #2d3540;
  }
  * { margin: 0; padding: 0; box-sizing: border-box; }
  html, body { width: 1200px; height: 750px; overflow: hidden; }
  body {
    position: relative;
    background: var(--white);
    font-family: "Open Sans", sans-serif;
    color: var(--text);
  }
  .brand {
    position: absolute; left: 117px; top: 44px;
    display: flex; align-items: center; gap: 10px;
  }
  .brand-mark { width: 14px; height: 14px; border-radius: 50%; background: var(--green); }
  .brand-name { font-size: 17px; font-weight: 600; color: var(--green); }
  .main-nav {
    position: absolute; top: 46px; left: 0; width: 100%;
    font-size: 12px;
  }
  .main-nav a {
    position: absolute; color: var(--dark); text-decoration: none; white-space: nowrap;
  }
  .main-nav a.active { font-weight: 600; }
  .main-nav a.active::after {
    content: ""; position: absolute; left: 0; right: 0; top: 25px;
    height: 2px; background: var(--green);
  }
  .login-button {
    position: absolute; left: 1002px; top: 40px; width: 83px; height: 29px;
    border: 1px solid var(--border); border-radius: 15px;
    font-size: 11px; color: var(--dark);
    display: flex; align-items: center; justify-content: center;
  }
  .hero-title {
    position: absolute; left: 113px; top: 128px;
    font-size: 63px; font-weight: 600; color: var(--dark); letter-spacing: -0.5px;
  }
  .title-rule {
    position: absolute; left: 117px; top: 212px; width: 150px; height: 2px;
    background: var(--green);
  }
  .slider-arrows { position: absolute; left: 116px; top: 236px; display: flex; gap: 10px; }
  .hero-intro {
    position: absolute; left: 279px; top: 204px; width: 410px;
    font-size: 13.3px; line-height: 26.7px; color: var(--text);
  }
  .hero-photo {
    position: absolute; left: 0; top: 321px; width: 1200px; height: 429px;
    background:
      radial-gradient(ellipse at 30% 40%, rgba(92,110,60,.55), transparent 55%),
      radial-gradient(ellipse at 75% 70%, rgba(120,150,160,.45), transparent 50%),
      linear-gradient(160deg, #8a7a62 0%, #5c5048 35%, #9c8a6c 60%, #4a4540 100%);
  }
  .contact-card {
    position: absolute; left: 852px; top: 168px; width: 231px; height: 305px;
    background: var(--green); border-radius: 3px; color: var(--white);
    padding: 33px 0 0 40px;
    box-shadow: 0 6px 20px rgba(0,0,0,.12);
  }
  .card-label {
    display: flex; align-items: center; gap: 8px;
    font-size: 10px; font-weight: 600; letter-spacing: 1.2px;
  }
  .card-label::after { content: ""; width: 42px; height: 1px; background: var(--white); }
  .card-address { margin-top: 14px; margin-left: -2px; font-size: 17px; line-height: 27px; }
  .card-label.contact { margin-top: 36px; }
  .contact-line {
    display: flex; align-items: center; gap: 5px; margin-left: -1px;
    font-size: 17px; line-height: 32px;
  }
  .contact-line.first { margin-top: 8px; }
  .contact-line.email { font-size: 13px; line-height: 24px; margin-top: 2px; }
</style>
</head>
<body>
  <header class="site-header">
    <a class="brand">
      <span class="brand-mark"></span>
      <span class="brand-name">Parc Lindehof</span>
    </a>
    <nav class="main-nav">
      <a class="active" style="left:496px">Home</a>
      <a style="left:551px">Het Park</a>
      <a style="left:618px">Financiering</a>
      <a style="left:706px">Chalets</a>
      <a style="left:767px">Aanbiedingen</a>
      <a style="left:864px">Faciliteiten</a>
      <a style="left:943px">Contact</a>
    </nav>
    <a class="login-button">Inloggen</a>
  </header>

  <section class="hero">
    <h1 class="hero-title">Chalet huren</h1>
    <div class="title-rule"></div>
    <div class="slider-arrows">
      <svg width="10" height="16" viewBox="0 0 10 16"><path d="M8 1 L2 8 L8 15" fill="none" stroke="#9aa0a6" stroke-width="1.5"/></svg>
      <svg width="10" height="16" viewBox="0 0 10 16"><path d="M2 1 L8 8 L2 15" fill="none" stroke="#6cb22f" stroke-width="1.5"/></svg>
    </div>
    <p class="hero-intro">Lorem ipsum dolor sit amet, consectetur adipiscing elit. Aenean euismod bibendum laoreet. Proin gravida dolor sit amet lacus accumsan et viverra justo commodo.</p>
    <div class="hero-photo" role="img" aria-label="Luchtfoto van een wijk met chalets en daken tussen groene bomen"></div>

    <aside class="contact-card">
      <div class="card-label">ADRESS</div>
      <p class="card-address">Bosrandlaan 14b<br>3912 PV Eikenrode</p>
      <div class="card-label contact">CONTACT</div>
      <div class="contact-line first">
        <svg width="11" height="11" viewBox="0 0 24 24"><path fill="#fff" d="M6.6 10.8a15.1 15.1 0 0 0 6.6 6.6l2.2-2.2c.3-.3.7-.4 1-.2 1.1.4 2.3.6 3.6.6.6 0 1 .4 1 1V20c0 .6-.4 1-1 1A17 17 0 0 1 3 4c0-.6.4-1 1-1h3.5c.6 0 1 .4 1 1 0 1.3.2 2.5.6 3.6.1.3 0 .7-.2 1z"/></svg>
        0123 - 45 67 80
      </div>
      <div class="contact-line">
        <svg width="11" height="11" viewBox="0 0 24 24"><path fill="#fff" d="M6.6 10.8a15.1 15.1 0 0 0 6.6 6.6l2.2-2.2c.3-.3.7-.4 1-.2 1.1.4 2.3.6 3.6.6.6 0 1 .4 1 1V20c0 .6-.4 1-1 1A17 17 0 0 1 3 4c0-.6.4-1 1-1h3.5c.6 0 1 .4 1 1 0 1.3.2 2.5.6 3.6.1.3 0 .7-.2 1z"/></svg>
        0123 - 45 98 21
      </div>
      <div class="contact-line email">
        <svg width="11" height="9" viewBox="0 0 22 16"><rect x="0" y="0" width="22" height="16" fill="#fff"/><path d="M1 1 L11 9 L21 1" fill="none" stroke="#6cb22f" stroke-width="2"/></svg>
        info@parclindehof.example
      </div>
    </aside>
  </section>
</body>
</html>
```